Tavenor Gymnastics Silver gym banner

We need a banner for our new gym.
It should have navy, light blue, lilac and purple colors with our name, logo and other wording in navy color. Colors should bleed one into the other.
File with name, logo and other wording is attached.
Words: Rhythmic gymnastics, ballet, etc should be on the bottom

Target Market(s)

Girls 3 to 16 years of age

Industry/Entity Type

Athletics

Font styles to use
Other font styles liked:
• Please use fonts on file included

Colors
0054AA
0677BA
7BADD7
CADEEF
E8F1F8
0094D4
00A9DD
6FCCEA
C7EBF8
E9F6FB
00AB8E
00BBA5
67D7C9
C6EFE9
E9F9F6
6B429C
8869AF
B7A5CE
E3DAEB
F3F0F8

Requirements
Must have
• our logo and name of the gym
Nice to have
• rhythmic gymnastics feel
Should not have
• bold colors

```html
<!DOCTYPE html>
<html lang="en">
<head>
<meta charset="utf-8">
<title>Tavenor Gymnastics – School of Champions Banner</title>
<link rel="stylesheet" href="https://fonts.googleapis.com/css2?family=Gentium+Book+Plus:wght@400;700&family=Marck+Script&display=swap">
<style>
  :root {
    --page-bg: #d6d6d8;
    --paper: #ffffff;
    --navy: #13279a;
    --ink: #2b2b33;
    --band: #4b4f9f;
    --band-text: #f3f0f8;
    --deep: #33366f;
    --violet: #6a52a8;
    --lilac: #b7a5ce;
    --lilac-bright: #9b7ee0;
    --bullet: #5a5aa6;
  }
  * { box-sizing: border-box; margin: 0; padding: 0; }
  html, body { width: 962px; height: 1200px; overflow: hidden; }
  body {
    background: var(--page-bg);
    font-family: "Gentium Book Plus", Georgia, serif;
    position: relative;
  }
  .banner {
    position: absolute;
    left: 31px; top: 375px;
    width: 900px; height: 450px;
    background: var(--paper);
    overflow: hidden;
    box-shadow: 0 10px 24px rgba(0,0,0,.28);
  }
  .banner__shape { position: absolute; inset: 0; }
  .brand-name {
    position: absolute; left: 50px; top: 44px;
    font-weight: 700; font-size: 30px; color: var(--navy);
  }
  .class-list {
    position: absolute; left: 52px; top: 118px;
    list-style: none;
  }
  .class-list li {
    display: flex; align-items: flex-start;
    font-weight: 700; font-size: 28px; line-height: 37px;
    color: var(--ink);
    margin-bottom: 4px;
  }
  .class-list svg { flex: none; width: 18px; height: 18px; margin: 9px 32px 0 0; }
  .web-band {
    position: absolute; left: 0; bottom: 0;
    width: 600px; height: 72px;
    background: var(--band);
    display: flex; align-items: center;
    padding-left: 46px;
    color: var(--band-text);
  }
  .web-band svg { width: 24px; height: 24px; margin-right: 16px; }
  .web-band span { font-size: 27px; letter-spacing: 2.6px; }
  .title {
    position: absolute; left: 462px; top: 14px;
    color: #fff; line-height: 1;
  }
  .title__main { display: block; font-weight: 700; font-size: 80px; letter-spacing: 1px; }
  .title__script {
    display: block; font-family: "Marck Script", cursive;
    font-size: 66px; margin: -8px 0 0 56px;
  }
  .photo {
    position: absolute;
    border-radius: 40% 40% 12px 12px;
  }
  .photo--ribbon {
    left: 345px; top: 135px; width: 140px; height: 235px;
    background: linear-gradient(160deg, rgba(240,226,120,.55), rgba(60,50,60,.35) 60%, rgba(210,170,140,.35));
  }
  .photo--dancers {
    left: 490px; top: 170px; width: 410px; height: 280px;
    background: linear-gradient(120deg, rgba(240,190,210,.45), rgba(230,90,170,.35) 45%, rgba(40,30,50,.35) 70%, rgba(200,130,220,.4));
  }
</style>
</head>
<body>
  <section class="banner" aria-label="Tavenor Gymnastics banner">
    <svg class="banner__shape" viewBox="0 0 900 450" preserveAspectRatio="none" aria-hidden="true">
      <defs>
        <linearGradient id="panelGradient" x1="0" y1="0" x2="1" y2="0.4">
          <stop offset="0" stop-color="var(--deep)"/>
          <stop offset="0.55" stop-color="#4e4595"/>
          <stop offset="1" stop-color="var(--violet)"/>
        </linearGradient>
      </defs>
      <path d="M430 0 C 360 60, 360 200, 470 290 C 540 350, 560 400, 575 450 L 560 450 C 545 400, 520 355, 455 295 C 345 200, 345 60, 415 0 Z" fill="var(--lilac-bright)"/>
      <path d="M445 0 C 380 60, 380 200, 485 285 C 555 345, 575 400, 590 450 L 900 450 L 900 0 Z" fill="url(#panelGradient)"/>
    </svg>

    <div class="brand-name">Tavenor Gymnastics</div>

    <ul class="class-list">
      <li><svg viewBox="0 0 18 18"><circle cx="9" cy="9" r="9" fill="var(--bullet)"/><path d="M4.5 9h8M9.5 5.5 13 9l-3.5 3.5" stroke="#fff" stroke-width="1.8" fill="none" stroke-linecap="round"/></svg>Rhythmic<br>Gymnastics</li>
      <li><svg viewBox="0 0 18 18"><circle cx="9" cy="9" r="9" fill="var(--bullet)"/><path d="M4.5 9h8M9.5 5.5 13 9l-3.5 3.5" stroke="#fff" stroke-width="1.8" fill="none" stroke-linecap="round"/></svg>Ballroom Dance</li>
      <li><svg viewBox="0 0 18 18"><circle cx="9" cy="9" r="9" fill="var(--bullet)"/><path d="M4.5 9h8M9.5 5.5 13 9l-3.5 3.5" stroke="#fff" stroke-width="1.8" fill="none" stroke-linecap="round"/></svg>Ballet</li>
      <li><svg viewBox="0 0 18 18"><circle cx="9" cy="9" r="9" fill="var(--bullet)"/><path d="M4.5 9h8M9.5 5.5 13 9l-3.5 3.5" stroke="#fff" stroke-width="1.8" fill="none" stroke-linecap="round"/></svg>Stretching</li>
      <li><svg viewBox="0 0 18 18"><circle cx="9" cy="9" r="9" fill="var(--bullet)"/><path d="M4.5 9h8M9.5 5.5 13 9l-3.5 3.5" stroke="#fff" stroke-width="1.8" fill="none" stroke-linecap="round"/></svg>Hip Hop</li>
    </ul>

    <div class="web-band">
      <svg viewBox="0 0 24 24" aria-hidden="true"><g fill="none" stroke="#fff" stroke-width="1.4"><circle cx="12" cy="12" r="10"/><ellipse cx="12" cy="12" rx="4.5" ry="10"/><path d="M2 12h20M4 6.5h16M4 17.5h16"/></g></svg>
      <span>www.tavenorgymnastics.com</span>
    </div>

    <div class="photo photo--ribbon" role="img" aria-label="Photo of a young rhythmic gymnast in a black leotard twirling a yellow ribbon"></div>
    <div class="photo photo--dancers" role="img" aria-label="Photo of a ballerina in a pink tutu, a hip hop dancer kicking high, an athlete lunging and a rhythmic gymnast with rainbow ribbons"></div>

    <h1 class="title">
      <span class="title__main">School of</span>
      <span class="title__script">Champions</span>
    </h1>
  </section>
</body>
</html>
```